Velkor Metrics Business Card project

We need a Business Card design for a brand new company called Velkor Metrics, based in Colombia, South America. In spanish, the name Velkor Metrics is built from Describing a Story with Data (Tejer OTRA Fábula con Cifras).
We recently finished our new logo project and now we need the business cards.
In VELKOR we generate knowledge from data. By producing an INTELLIGENT VISUALIZATION of our clients´ data we create AWARENESS of their business environment. We drive GROWTH through DATA VISUALIZATION.
We are a service provider of Data Science, Business Intelligence and Visualization and we are breaking mental barriers in our culture and our market. It is an innovative way to use this services procuring mid term contracts to take our clients in a data based journey to understand their environment. We awe our clients with our data driven insights and our state of the art visualizations
We would like our clients to be seen as: Knowledgable, Dynamic, Fresh, Smart, Acute, Open minded, Brainy, Evolving
Our core has this 4 words: Visual, Knowledgable, Mathematician, Genius
Our brand personality is: Young (early 30s), Brainy, Easy going, Street smart, Creative, Mind blowing, Very Techie, Fun, Social, Uncomplicated
Our promise: we deliver data driven insights using state-of-the-art computer modeling and creative analysis.
This is the first step and the milestone to build all our graphic future (website, mail signature, banners, envelopes, Templates, etc)
It is a face to face sale with cloud based reports and visualizations
There is a similar company that has done great and we want to emulate but we must be different: www.pilvoraq.co
Target Market(s)
Business Intelligence managers, Upper level management, General managers, IT heads and graphic designers
Industry/Entity Type
Computer
Look and feel

```html
<!DOCTYPE html>
<html lang="en">
<head>
<meta charset="utf-8">
<title>Velkor Metrics – Business Card</title>
<link rel="stylesheet" href="https://fonts.googleapis.com/css2?family=Archivo+Black&family=Montserrat:wght@400;500&display=swap">
<style>
  :root {
    --orange-light: #f7941d;
    --orange-deep: #f15a29;
    --brand-orange: #f47a25;
    --ink: #111111;
    --paper: #ffffff;
  }
  * { margin: 0; padding: 0; box-sizing: border-box; }
  html, body {
    width: 1200px;
    height: 692px;
    overflow: hidden;
    background: var(--paper);
  }
  .card {
    position: relative;
    width: 1200px;
    height: 692px;
    background: var(--paper);
    font-family: "Montserrat", sans-serif;
    color: var(--ink);
  }
  .brand {
    position: absolute;
    left: 57px;
    top: 60px;
  }
  .brand-dot {
    display: block;
    width: 72px;
    height: 72px;
    border-radius: 50%;
    background: var(--brand-orange);
    margin: 0 0 30px 68px;
  }
  .brand-name {
    font-family: "Montserrat", sans-serif;
    font-weight: 500;
    font-size: 40px;
    letter-spacing: -0.5px;
    color: var(--brand-orange);
    line-height: 1;
  }
  .person-name {
    position: absolute;
    left: 728px;
    top: 305px;
    font-family: "Archivo Black", sans-serif;
    font-size: 50px;
    letter-spacing: 1px;
    line-height: 1;
    transform: scaleX(1.12);
    transform-origin: left center;
  }
  .name-rule {
    position: absolute;
    left: 680px;
    top: 370px;
    width: 520px;
    height: 18px;
    background: linear-gradient(90deg, var(--orange-light), var(--orange-deep));
  }
  .person-title {
    position: absolute;
    left: 774px;
    top: 400px;
    font-size: 22px;
    font-weight: 400;
    letter-spacing: 7px;
    line-height: 1;
  }
  .contact-band {
    position: absolute;
    left: 0;
    top: 590px;
    width: 1200px;
    height: 58px;
    display: flex;
    align-items: center;
    justify-content: center;
    gap: 30px;
    background: linear-gradient(90deg, var(--orange-light), var(--orange-deep));
    color: var(--paper);
    font-size: 27px;
    font-weight: 400;
    line-height: 58px;
    white-space: nowrap;
  }
  .contact-sep { font-weight: 400; }
</style>
</head>
<body>
  <div class="card">
    <div class="brand">
      <span class="brand-dot" aria-hidden="true"></span>
      <div class="brand-name">Velkor Metrics</div>
    </div>

    <div class="person-name">Teodoro</div>
    <div class="name-rule" aria-hidden="true"></div>
    <div class="person-title">DIRECTOR</div>

    <div class="contact-band">
      <span class="contact-phone">Ph. 321-654987</span>
      <span class="contact-sep" aria-hidden="true">|</span>
      <span class="contact-email">teodoro@velkormetrics.com</span>
      <span class="contact-sep" aria-hidden="true">|</span>
      <span class="contact-web">www.velkormetrics.com</span>
    </div>
  </div>
</body>
</html>
```